Need simple and modern looking business card with all my information on one side and logo on the other side
Info :
Company name - VELMAR CONSTRUCTION LLC
Company addres- 418 harbor 87th. Dunmoor park ny 10352
Email- velmarllc@tridomail.Com
Company phone number 555-318-6094
Cell number- 555-742-0583
Web site - velmarllc.Com
My name Gerald tomasino

Target Market(s)

Construction , home improvement, remodeling

Industry/Entity Type

Construction

Contact Information for Business Card

It has to be moder but at the same time simple

Font styles to use
Sans Serif

Colors
0255a3
ffffff
000000
f78f20
b1b1b1
9d9d9d
1b1b1b
33a6d7
ec1f27

Requirements
Must have
• My logo on one side maybe with a some kind of background on the other side all my information
Nice to have
• Some kind of background pictures provided by you .PLEASE HAVE ACCOUNT WITH PIXELVAULT WILL NOT PAY ANY EXTRA FEES .
Should not have
• Any kind of hamer, nails,screws, helmets itp. Please do not copy the other designs come up with something new.

```html
<!DOCTYPE html>
<html lang="en">
<head>
<meta charset="utf-8">
<title>Velmar Construction LLC – Business Card</title>
<link rel="stylesheet" href="https://fonts.googleapis.com/css2?family=Jost:wght@400;500&family=Open+Sans:wght@400&display=swap">
<style>
  :root {
    --stage: #8f9194;
    --card-white: #ffffff;
    --card-dark: #231512;
    --ink: #1b1b1b;
    --ink-soft: #3a3a3a;
    --muted: #6b6b6b;
    --orange: #f78f20;
    --black: #000000;
    --shadow: rgba(0, 0, 0, 0.28);
  }
  * { box-sizing: border-box; margin: 0; padding: 0; }
  html, body {
    width: 1200px;
    height: 900px;
    overflow: hidden;
    background: var(--stage);
  }
  .canvas {
    position: relative;
    width: 1200px;
    height: 900px;
    display: flex;
    flex-direction: column;
    align-items: center;
    justify-content: center;
    gap: 40px;
  }
  .card {
    position: relative;
    width: 630px;
    height: 360px;
    box-shadow: 0 10px 30px var(--shadow);
    overflow: hidden;
  }

  /* Front side */
  .card--front { background: var(--card-white); }
  .brand {
    position: absolute;
    left: 258px;
    top: 52px;
    display: flex;
    align-items: center;
    gap: 8px;
  }
  .brand__mark {
    width: 14px;
    height: 14px;
    background: var(--orange);
  }
  .brand__name {
    font-family: "Jost", sans-serif;
    font-weight: 500;
    font-size: 17px;
    letter-spacing: 0.04em;
    color: var(--ink);
  }
  .accent-bar { position: absolute; height: 9px; }
  .accent-bar--orange { left: 0; top: 150px; width: 228px; background: var(--orange); }
  .accent-bar--black { right: 0; top: 96px; width: 140px; background: var(--black); }
  .person {
    position: absolute;
    left: 225px;
    top: 112px;
    width: 300px;
    text-align: center;
  }
  .person__name {
    font-family: "Jost", sans-serif;
    font-weight: 400;
    font-size: 30px;
    line-height: 1.1;
    color: var(--ink);
  }
  .person__title {
    margin-top: 4px;
    font-family: "Jost", sans-serif;
    font-size: 9px;
    letter-spacing: 0.34em;
    color: var(--muted);
  }
  .contact {
    position: absolute;
    font-family: "Open Sans", sans-serif;
    color: var(--ink-soft);
  }
  .contact--phones {
    right: 32px;
    top: 170px;
    text-align: right;
    font-size: 12.5px;
    line-height: 1.45;
  }
  .contact--address {
    left: 44px;
    top: 244px;
    font-size: 15px;
    line-height: 1.45;
    color: var(--ink);
  }

  /* Back side */
  .card--back {
    background: var(--card-dark);
    display: flex;
    align-items: center;
    justify-content: center;
  }
  .brand--reverse {
    position: static;
    gap: 12px;
  }
  .brand--reverse .brand__mark { width: 22px; height: 22px; }
  .brand--reverse .brand__name {
    font-size: 30px;
    color: var(--card-white);
  }
</style>
</head>
<body>
<main class="canvas">
  <section class="card card--front" aria-label="Business card front">
    <div class="brand">
      <span class="brand__mark"></span>
      <span class="brand__name">VELMAR CONSTRUCTION LLC</span>
    </div>
    <span class="accent-bar accent-bar--black"></span>
    <div class="person">
      <h1 class="person__name">Gerald tomasino</h1>
      <p class="person__title">MANAGING DIRECTOR</p>
    </div>
    <span class="accent-bar accent-bar--orange"></span>
    <address class="contact contact--phones">
      Phone:&nbsp; 555-318-6094<br>
      Cell number: 555-742-0583<br>
      velmarllc@tridomail.com
    </address>
    <address class="contact contact--address">
      418 harbor 87th.<br>
      Dunmoor park ny 10352<br>
      www.velmarllc.com
    </address>
  </section>

  <section class="card card--back" aria-label="Business card back">
    <div class="brand brand--reverse">
      <span class="brand__mark"></span>
      <span class="brand__name">VELMAR CONSTRUCTION LLC</span>
    </div>
  </section>
</main>
</body>
</html>
```